BRASKETT LAND SERVICES BILLBOARD DESIGN

I NEED A BILLBOARD FOR MY BUSINESS. WE ARE A LAND CLEARING COMPANY AND I WOULD LIKE TO ADD A PICTURE OF MY TRACK LOADER TO THE SIGN. OPEN TO COLORS. I WOULD ALSO LIKE TO HAVE MY PHONE NUMBER 555-284-7196, WEBSITE WWW.BRASKETTLANDSERVICES.EXAMPLE, AND EMAIL ON THE SIGN (CONTACT@BRASKETTLANDSERVICES.EXAMPLE). DESIGNERS CAN HAVE THE FREEDOM TO DO WHATEVER STYLE THEY WANT AND TO USE ANY COLORS THEY WANT.

Target Market(s)

ANYONE WITH PROPERTY

Requirements
Must have
• PICTURE OF TRACK LOADER, WEBSITE, PHONE NUMBER, EMAIL
Nice to have
• OPEN TO ANYTHING
Should not have
• OPEN TO ANYTHING

```html
<!DOCTYPE html>
<html lang="en">
<head>
<meta charset="utf-8">
<title>Braskett Land Services Billboard</title>
<link href="https://fonts.googleapis.com/css2?family=Saira+Condensed:wght@800&family=Montserrat:wght@700&display=swap" rel="stylesheet">
<style>
  :root {
    --page-bg: #e9e7e2;
    --panel-white: #ffffff;
    --ink: #1f1c17;
    --band-olive: #4a4538;
    --text-light: #ffffff;
    --forest-top: #5f7a4a;
    --forest-mid: #3f5a33;
    --meadow: #8f8a55;
  }
  html, body {
    margin: 0;
    width: 1200px;
    height: 900px;
    overflow: hidden;
    background: var(--page-bg);
  }
  .billboard {
    position: absolute;
    left: 0;
    top: 170px;
    width: 1200px;
    height: 560px;
    background: var(--panel-white);
    overflow: hidden;
  }
  .billboard-shapes {
    position: absolute;
    inset: 0;
  }
  .company-name {
    position: absolute;
    left: 36px;
    top: 24px;
    margin: 0;
    font-family: "Saira Condensed", "Arial Narrow", sans-serif;
    font-weight: 800;
    font-size: 84px;
    line-height: 0.86;
    color: var(--ink);
    letter-spacing: 1px;
  }
  .call-band {
    position: absolute;
    left: 0;
    top: 200px;
    width: 545px;
    height: 262px;
    background: var(--band-olive);
  }
  .call-label,
  .call-number {
    position: absolute;
    left: 36px;
    margin: 0;
    font-family: "Saira Condensed", "Arial Narrow", sans-serif;
    font-weight: 800;
    color: var(--text-light);
    line-height: 1;
    font-size: 94px;
    white-space: nowrap;
  }
  .call-label { top: 218px; }
  .call-number { top: 336px; letter-spacing: 1px; }
  .website {
    position: absolute;
    left: 36px;
    top: 486px;
    margin: 0;
    font-family: "Saira Condensed", "Arial Narrow", sans-serif;
    font-weight: 800;
    font-size: 29px;
    line-height: 1;
    color: var(--ink);
    letter-spacing: 0.5px;
    white-space: nowrap;
  }
  .email {
    position: absolute;
    right: 30px;
    bottom: 16px;
    margin: 0;
    font-family: "Montserrat", Arial, sans-serif;
    font-weight: 700;
    font-size: 27px;
    line-height: 1.3;
    color: var(--text-light);
    white-space: nowrap;
  }
</style>
</head>
<body>
  <div class="billboard">
    <svg class="billboard-shapes" width="1200" height="560" viewBox="0 0 1200 560">
      <defs>
        <linearGradient id="loaderPhotoTone" x1="0" y1="0" x2="0" y2="1">
          <stop offset="0" stop-color="var(--forest-top)"/>
          <stop offset="0.55" stop-color="var(--forest-mid)"/>
          <stop offset="1" stop-color="var(--meadow)"/>
        </linearGradient>
      </defs>
      <g role="img" aria-label="Photo of an orange tracked loader with a forestry mulcher head on a cleared lot in front of trees">
        <polygon points="662,0 1200,0 1200,560 602,560" fill="url(#loaderPhotoTone)"/>
      </g>
      <polygon class="divider-stripe" points="615,0 650,0 590,560 555,560" fill="var(--ink)"/>
      <polygon class="email-strip" points="597,492 1200,492 1200,560 590,560" fill="var(--ink)"/>
    </svg>

    <h1 class="company-name">BRASKETT LAND<br>SERVICES</h1>
    <div class="call-band"></div>
    <p class="call-label">CALL NOW</p>
    <p class="call-number">555-284-7196</p>
    <p class="website">WWW.BRASKETTLANDSERVICES.EXAMPLE</p>
    <p class="email">contact@braskettlandservices.example</p>
  </div>
</body>
</html>
```